Redesign Teeth Whitening Flyer

I need to redesign this flyer attached. I have upgraded the kit. Logo attached and current design uploaded. I have new content etc that I will provide in the brief. Here is a competitor of mine that does well https://www.krovimart.example/Plinq-Teeth-Whitening-At-Home-Sensitivity/dp/Q48RT21K7M

The size will be full bleed: 7.875" X 4.375"

FULL COLOR
Front & Back

FRONT SIDE:
~~VEXT LOGO~~
~~PLEASE INTEGRATE PHOTOS OF THE PRODUCT I HAVE ATTACHED. I GOT THESE PHOTOS FROM THE MANUFACTURERS WEBSITES. PLEASE KEEP IN MIND THIS WILL BE PRINTED~~

CONTENT:
ADVANCED TEETH WHITENING SYSTEM
15 TREATMENTS INCLUDED

BACK SIDE CONTENT:
Thank you for your purchase of Vext Professional Teeth Whitening products. All of our whitening solutions are manufactured in a BRQ registered facility in the USA.

We provide effective and affordable teeth whitening solutions using the highest quality ingredients available.

Directions:

Step 1
Rinse the LED Smart Tray with warm water.

Step 2
Apply whitening solution to your teeth. Rotate the pen at the base to dispense the gel onto the brush. Make a big wide smile and apply the gel generously to the teeth using the brush. Be sure to apply the whitening gel to the front of the teeth only.

Step 3
Connect the LED Smart Tray to any smart device or power bank of your choice and turn it on so that the LED light is constant.

Step 4
Put the Smart Tray into your mouth and bite down firmly. Keep the tray in your mouth for 20-30 minutes.

Step 5
Remove the tray from your mouth and rinse your mouth and tray with lukewarm water and allow the tray to dry before storing it.

There are up to 15 treatments included with one pen.

We recommend when using the system for the first time to use it daily until desired results are achieved. Then reduce to 1-2 times per week to maintain.

To get more whitening solution pens please go to www.VextTeethWhitening.example

DISCLAIMERS:
Keep out of reach of children. Avoid contact with eyes and skin. Consult your dentist before using. Do not use if pregnant, lactating, have gum disease or other dental conditions. Discontinue use if pain on teeth or gums occurs. Use only as instructed. Use at your own risk. Purchasing any of our products frees all distributors, manufacturers and affiliates from any liability associated with the use of this system. Do not use if you are allergic to peroxide products. The whitening solution is a 12% Hydrogen Peroxide whitening solution. 12% HP is equivalent to 36% Carbamide Peroxide. A temporary side effect of tooth sensitivity or mild tissue irritation is possible but usually transient and may last for a day or two. Avoid beverages that contain citrus and hot and cold drinks for the next 24 hours after treatment. Sticking to room temperature drinks is ideal. If you have any adverse reactions terminate the use of this product and consult a healthcare professional.

Target Market(s)

consumers that are interested in teeth whitening home kits. DIY teeth whitening at home

Font styles to use
Other font styles liked:
• open

Requirements
Must have
• FULL COLOR
Front & Back

FRONT SIDE:
~~VEXT LOGO~~

CONTENT:
15 TREATMENTS INCLUDED

BACK SIDE CONTENT:

Directions:

Step 1

Step 2

Step 3

Step 4

Step 5

DISCLAIMERS:
Nice to have
• FULL COLOR
Front & Back

FRONT SIDE:
~~VEXT LOGO~~

CONTENT:
15 TREATMENTS INCLUDED

BACK SIDE CONTENT:

Directions:

Step 1

Step 2

Step 3

Step 4

Step 5

DISCLAIMERS:

```html
<!DOCTYPE html>
<html lang="en">
<head>
<meta charset="utf-8">
<title>Vext Advanced Teeth Whitening System – Flyer</title>
<link href="https://fonts.googleapis.com/css2?family=Poppins:wght@500;600;700&family=Catamaran:wght@400;600;700&display=swap" rel="stylesheet">
<style>
  :root{
    --page:#e8f2f9;
    --blue:#2fa0dc;
    --blue-deep:#2a93d2;
    --blue-light:#c1e4f8;
    --ink-dark:#333333;
    --grey:#9a9a9a;
    --white:#ffffff;
    --pale-text:#e4f4fe;
  }
  *{margin:0;padding:0;box-sizing:border-box}
  html,body{width:1200px;height:1200px;overflow:hidden;background:var(--page)}
  .sheet{position:relative;width:1200px;height:1200px}
  .card{position:absolute;top:159px;width:473px;height:849px;overflow:hidden;background:var(--white);box-shadow:0 3px 10px rgba(40,70,100,.18)}
  .card--front{left:84px}
  .card--back{left:634px}
  .card__shapes{position:absolute;inset:0;width:473px;height:849px}

  .brand{position:absolute;left:255px;top:33px;width:190px;text-align:center}
  .brand__name{display:block;font-family:"Poppins",sans-serif;font-weight:600;font-size:46px;line-height:46px;letter-spacing:4px;color:var(--blue)}
  .brand__tag{display:block;margin-top:2px;font-family:"Catamaran",sans-serif;font-weight:400;font-size:8px;letter-spacing:2.4px;color:#6a6a6a;white-space:nowrap}

  .headline{position:absolute;right:42px;top:536px;text-align:right;font-family:"Poppins",sans-serif;font-weight:700;font-size:62px;line-height:59px;letter-spacing:-.5px}
  .headline span{display:block}
  .headline .tone-light{color:var(--blue-light)}
  .headline .tone-white{color:var(--white)}
  .offer{position:absolute;left:58px;top:782px;font-family:"Poppins",sans-serif;font-weight:700;font-size:24px;line-height:26px;color:var(--white);white-space:nowrap}
  .offer__count{color:var(--blue-deep)}

  .back-text{font-family:"Catamaran",sans-serif}
  .thanks{position:absolute;left:12px;right:12px;top:100px;text-align:center;font-weight:700;font-size:10.8px;line-height:13.4px;color:var(--blue)}
  .mission{position:absolute;left:8px;right:8px;top:146px;text-align:center;font-weight:700;font-size:10.8px;line-height:13.4px;color:var(--grey)}
  .directions__title{position:absolute;left:96px;top:182px;font-weight:700;font-size:18px;line-height:22px;color:var(--blue)}
  .step{position:absolute;left:29px;width:420px;display:flex;gap:7px}
  .step__tag{flex:none;width:53px;height:20px;background:var(--blue);color:var(--white);font-weight:700;font-size:12px;line-height:21px;text-align:center}
  .step__text{font-weight:400;font-size:11.4px;line-height:13.5px;color:var(--blue);padding-top:1px}

  .note{position:absolute;right:20px;text-align:right;font-weight:600;font-size:12.4px;line-height:13.5px;color:var(--pale-text);text-transform:uppercase;white-space:nowrap}
  .note--count{top:490px}
  .note--plan{top:524px}
  .reorder{position:absolute;left:31px;top:615px;font-weight:600;font-size:10.9px;line-height:16px;color:var(--white);display:flex;align-items:center;gap:4px;white-space:nowrap}
  .reorder__link{background:var(--blue-light);color:var(--blue);font-weight:700;border-radius:9px;padding:0 6px;line-height:16px}
  .disclaimer__title{position:absolute;left:32px;top:653px;font-weight:700;font-size:13.5px;line-height:16px;color:var(--white)}
  .disclaimer__body{position:absolute;left:32px;top:669px;font-weight:400;font-size:10.2px;line-height:13.5px;color:var(--white)}
  .disclaimer__body span{display:block;white-space:nowrap}
</style>
</head>
<body>
<main class="sheet">

  <!-- FRONT -->
  <section class="card card--front" aria-label="Flyer front">
    <svg class="card__shapes" viewBox="0 0 761 1367" preserveAspectRatio="none">
      <defs>
        <linearGradient id="photoTone" x1="0" y1="0" x2="1" y2="1">
          <stop offset="0" stop-color="#d9e2cf"/>
          <stop offset=".45" stop-color="#d8c3ad"/>
          <stop offset="1" stop-color="#ece7e1"/>
        </linearGradient>
        <radialGradient id="kitToneFront" cx=".5" cy=".5" r=".6">
          <stop offset="0" stop-color="#d6effb"/>
          <stop offset="1" stop-color="#eef4f8"/>
        </radialGradient>
      </defs>
      <g role="img" aria-label="Photo of a smiling couple">
        <rect x="0" y="0" width="761" height="900" fill="url(#photoTone)"/>
      </g>
      <polygon points="0,824 761,590 761,660 0,894" fill="var(--ink-dark)"/>
      <polygon points="0,894 761,660 761,1367 0,1367" fill="var(--blue)"/>
      <polygon points="610,690 761,660 761,916" fill="var(--blue-light)"/>
      <polygon points="0,1139 0,1367 242,1367" fill="var(--blue-light)"/>
      <circle cx="562" cy="737" r="112" fill="var(--white)" stroke="var(--blue)" stroke-width="8"/>
      <g role="img" aria-label="Product photo: LED smart tray connected to a phone with whitening pen">
        <circle cx="562" cy="737" r="100" fill="url(#kitToneFront)"/>
      </g>
      <polyline points="599,1277 719,1277 719,874" fill="none" stroke="var(--white)" stroke-width="2"/>
    </svg>

    <div class="brand">
      <span class="brand__name">VEXT</span>
      <span class="brand__tag">PROFESSIONAL TEETH WHITENING</span>
    </div>

    <h1 class="headline">
      <span class="tone-light">ADVANCED</span>
      <span class="tone-white">TEETH</span>
      <span class="tone-white">WHITENING</span>
      <span class="tone-light">SYSTEM</span>
    </h1>
    <p class="offer"><span class="offer__count">15</span> TREATMENTS INCLUDED</p>
  </section>

  <!-- BACK -->
  <section class="card card--back back-text" aria-label="Flyer back">
    <svg class="card__shapes" viewBox="0 0 761 1367" preserveAspectRatio="none">
      <defs>
        <radialGradient id="kitToneBack" cx=".5" cy=".5" r=".6">
          <stop offset="0" stop-color="#d6effb"/>
          <stop offset="1" stop-color="#eef4f8"/>
        </radialGradient>
      </defs>
      <polygon points="0,0 219,0 0,189" fill="var(--blue-light)"/>
      <polyline points="144,314 47,314 47,760" fill="none" stroke="var(--blue)" stroke-width="3"/>
      <polygon points="0,820 761,650 761,662 0,894" fill="var(--ink-dark)"/>
      <polygon points="0,894 761,662 761,1367 0,1367" fill="var(--blue)"/>
      <polygon points="0,1164 0,1367 245,1367" fill="var(--blue-light)"/>
      <circle cx="147" cy="829" r="111" fill="var(--white)" stroke="var(--blue)" stroke-width="8"/>
      <g role="img" aria-label="Product photo: LED smart tray connected to a phone with whitening pen">
        <circle cx="147" cy="829" r="99" fill="url(#kitToneBack)"/>
      </g>
    </svg>

    <div class="brand" style="left:257px;top:34px">
      <span class="brand__name">VEXT</span>
      <span class="brand__tag">PROFESSIONAL TEETH WHITENING</span>
    </div>

    <p class="thanks">THANK YOU FOR YOUR PURCHASE OF VEXT PROFESSIONAL TEETH WHITENING<br>PRODUCTS. ALL OF OUR WHITENING SOLUTIONS ARE MANUFACTURED IN A<br>BRQ REGISTERED FACILITY IN THE USA.</p>
    <p class="mission">WE PROVIDE EFFECTIVE AND AFFORDABLE TEETH WHITENING SOLUTIONS USING THE<br>HIGHEST QUALITY INGREDIENTS AVAILABLE.</p>

    <h2 class="directions__title">DIRECTIONS</h2>
    <div class="step" style="top:218px"><span class="step__tag">STEP 1</span><p class="step__text">Rinse the LED Smart Tray with warm water.</p></div>
    <div class="step" style="top:251px"><span class="step__tag">STEP 2</span><p class="step__text">Apply whitening solution to your teeth. Rotate the pen at the base to dispense the gel onto the brush. Make a big wide smile and apply the gel generously to the teeth using the brush. Be sure to apply the whitening gel to the front of the teeth only.</p></div>
    <div class="step" style="top:319px"><span class="step__tag">STEP 3</span><p class="step__text">Connect the LED Smart Tray to any smart device or power bank of your choice and turn it on so that the LED light is constant.</p></div>
    <div class="step" style="top:360px"><span class="step__tag">STEP 4</span><p class="step__text">Put the Smart Tray into your mouth and bite down firmly. Keep the tray in your mouth for 20-30 minutes.</p></div>
    <div class="step" style="top:400px"><span class="step__tag">STEP 5</span><p class="step__text">Remove the tray from your mouth and rinse your mouth and tray with<br>lukewarm water and allow the tray to dry before storing it.</p></div>

    <p class="note note--count">There are up to<br>15 treatments included with one pen</p>
    <p class="note note--plan">We recommend when using the system for<br>then first time to use it daily until desired<br>results are achieved.Then reduce to<br>1-2 timesper week to maintain</p>

    <p class="reorder">To get more whitening solution pens please go to <span class="reorder__link">www.VextTeethWhitening.example</span></p>

    <h3 class="disclaimer__title">DISCLAIMERS</h3>
    <p class="disclaimer__body">
      <span>Keep out of reach of children. Avoid contact with eyes and skin. Consult your dentist before using.</span>
      <span>Do not use if pregnant, lactating, have gum disease or other dental conditions. Discontinue use if</span>
      <span>pain on teeth or gums occurs. Use only as instructed. Use at your own risk. Purchasing any of our</span>
      <span>products frees all distributors, manufacturers and affiliates from any liability associated with the</span>
      <span style="margin-left:5px">use of this system. Do not use if you are allergic to peroxide products. The whitening solution is a</span>
      <span style="margin-left:17px">12% Hydrogen Peroxide whitening solution. 12% HP is equivalent to 36% Carbamide Peroxide.</span>
      <span style="margin-left:31px">A temporary side effect of tooth sensitivity or mild tissue irritation is possible but usually</span>
      <span style="margin-left:45px">transient and may last for a day or two. Avoid beverages that contain citrus and hot</span>
      <span style="margin-left:57px">and cold drinks for the next 24 hours after treatment. Sticking to room temperature</span>
      <span style="margin-left:70px">drinks is ideal. If you have any adverse reactions terminate the use of this product</span>
      <span style="margin-left:86px">and consult a healthcare professional.</span>
    </p>
  </section>

</main>
</body>
</html>
```